GiftHarbor Capabilities Deck - Build Powerpoint Template

Hello - we need to build a capabilities deck to send to potential buyers. We have the information and need a deck built that reflects our logo and design language. We should be able to edit the powerpoint as needed and updates are required.

Target Market(s)

Marketing Teams, Sales Development Teams, HR - anyone who needs swag/merch

Font styles to use
Serif
Sans Serif

Colors
0054AA
0677BA
7BADD7
CADEEF
E8F1F8

Requirements
Must have
• Clean design reflecting our logo and highlighting our merch
Should not have
• avoid word-heavy slides, obvious AI-designs

```html
<!DOCTYPE html>
<html lang="en">
<head>
<meta charset="utf-8">
<title>GiftHarbor Capabilities Deck</title>
<link href="https://fonts.googleapis.com/css2?family=Poppins:wght@400;500;600;700;800&display=swap" rel="stylesheet">
<style>
:root{
  --blue:#0a3ba7;
  --blue-deep:#08359a;
  --teal:#25d8cf;
  --teal-soft:#b8f6f1;
  --lavender:#c9cdf0;
  --ink:#111;
  --text:#222;
  --sheet-left:#ffffff;
  --sheet-right:#ececec;
}
*{margin:0;padding:0;box-sizing:border-box}
html,body{width:1032px;height:1200px;overflow:hidden}
body{position:relative;font-family:'Poppins',sans-serif;color:var(--text);
  background:linear-gradient(90deg,var(--sheet-left) 0 531px,var(--sheet-right) 531px)}
.slide{position:absolute;width:452px;height:254px;overflow:hidden;
  background:
    radial-gradient(ellipse 55% 45% at 8% 95%,rgba(170,172,225,.75),transparent 70%),
    radial-gradient(ellipse 45% 60% at 100% 15%,rgba(150,240,232,.8),transparent 70%),
    linear-gradient(115deg,#f6f5ff 0%,#e6f6fc 45%,#c8f9f6 100%)}
.col-l{left:60px}.col-r{left:533px}
.row1{top:32px}.row2{top:318px}.row3{top:606px}.row4{top:892px}
.abs{position:absolute}
.brand{position:absolute;display:flex;align-items:center;gap:4px;font-weight:600;color:var(--blue);white-space:nowrap}
.brand .dot{width:.62em;height:.62em;border-radius:50%;background:var(--teal)}
.brand-sm{font-size:12px;top:9px;right:38px}
.heading{position:absolute;left:38px;font-weight:700;color:var(--blue);font-size:14px}
.body{position:absolute;left:38px;font-size:4.6px;line-height:9.4px;color:var(--text)}
.footer{position:absolute;left:0;bottom:0;width:100%;height:18px;background:var(--blue-deep);font-size:4.6px;color:#fff}
.footer .band{position:absolute;right:0;top:0;height:100%;width:139px;background:var(--teal);clip-path:polygon(11px 0,100% 0,100% 100%,0 100%)}
.footer .mail{position:absolute;left:38px;top:6px;display:flex;align-items:center;gap:2px}
.footer .page{position:absolute;right:39px;top:6px;color:#e9fffd}
.ph{position:absolute}
.cover-title{position:absolute;width:100%;text-align:center;font-weight:800;color:var(--ink)}
.agenda-panel{position:absolute;left:0;top:0;width:166px;height:100%;background:var(--blue-deep)}
.agenda-panel h2{position:absolute;left:38px;top:101px;color:#fff;font-size:13.5px;line-height:18px;font-weight:700}
.agenda{position:absolute;left:241px;top:35px;width:178px;list-style:none}
.agenda li{display:flex;height:19.6px;align-items:center;border-bottom:.6px solid #4a5a7a;font-size:7px;font-weight:500;color:var(--ink)}
.agenda li span{width:27px}
.big-circle{position:absolute;border-radius:50%;background:var(--blue-deep);color:#fff;display:flex;align-items:center;justify-content:center;font-weight:700;text-align:center}
.service{position:absolute}
.service .icon{position:absolute;left:-16px;top:0;width:23px;height:23px;margin-left:-11.5px;border-radius:50%;background:var(--teal);display:flex;align-items:center;justify-content:center}
.service h4{font-size:5.4px;font-weight:600;color:var(--ink);margin-bottom:3px}
.service p{font-size:4.5px;line-height:8.2px}
.step{position:absolute;top:103px;width:82px}
.step .icon{width:18px;height:14px;display:flex;align-items:center;justify-content:center;margin-left:2px;background:radial-gradient(circle,rgba(37,216,207,.35),transparent 70%)}
.step h4{font-size:5.4px;font-weight:600;color:var(--ink);margin:3px 0 6px}
.step p{font-size:4.5px;line-height:8.2px}
.reason{position:absolute;width:84px}
.reason h4{font-size:5.4px;font-weight:600;color:var(--ink);margin-bottom:3px}
.reason p{font-size:4.5px;line-height:8.2px}
.reason.left{text-align:right}
.node{position:absolute;width:13px;height:13px;border-radius:50%;background:var(--teal);margin:-6.5px 0 0 -6.5px}
.contact-disc{position:absolute;left:189px;top:137px;width:74px;height:74px;border-radius:50%;background:#fff;display:flex;flex-direction:column;align-items:center;justify-content:center;font-size:4.6px;font-weight:600;line-height:9.4px;color:var(--ink)}
</style>
</head>
<body>

<!-- Cover -->
<section class="slide col-l row1">
  <div class="ph" role="img" aria-label="Branded tumbler product photo" style="left:74px;top:24px;width:42px;height:42px;border-radius:50%;background:linear-gradient(135deg,#3a4a66,#1e2a3e)"></div>
  <div class="ph" role="img" aria-label="Pink lip balm product photo" style="left:202px;top:14px;width:54px;height:40px;border-radius:50%;background:linear-gradient(135deg,#f070c0,#e23597)"></div>
  <div class="ph" role="img" aria-label="Branded water bottle product photo" style="left:333px;top:12px;width:42px;height:64px;border-radius:18px;background:linear-gradient(160deg,#2aa0b8,#0e5f7a)"></div>
  <div class="ph" role="img" aria-label="Black tote bag product photo" style="left:24px;top:102px;width:51px;height:75px;border-radius:8px;background:linear-gradient(160deg,#2a2a2a,#111)"></div>
  <div class="ph" role="img" aria-label="Printed mug product photo" style="left:364px;top:143px;width:44px;height:44px;border-radius:50%;background:linear-gradient(135deg,#f7e3b5,#e9c985)"></div>
  <div class="ph" role="img" aria-label="Blue polo shirt product photo" style="left:113px;top:180px;width:58px;height:62px;border-radius:40%;background:linear-gradient(135deg,#2fc6ef,#1591c6)"></div>
  <div class="ph" role="img" aria-label="Grey backpack product photo" style="left:256px;top:183px;width:52px;height:54px;border-radius:45%;background:linear-gradient(135deg,#5a5d63,#2f3136)"></div>
  <div class="brand" style="font-size:17px;left:0;right:0;top:85px;justify-content:center"><i class="dot"></i>GiftHarbor</div>
  <div class="abs" style="left:170px;top:115px;width:112px;height:.6px;background:#9aa6c0"></div>
  <h1 class="cover-title" style="top:127px;font-size:15.5px">YOUR BRAND. MAGNETIZED.</h1>
  <p class="cover-title" style="top:153px;font-size:7.3px;font-weight:500;color:var(--blue)">Custom Merchandise That Moves People.</p>
</section>

<!-- Agenda -->
<section class="slide col-r row1">
  <div class="agenda-panel"><h2>Here<br>Goes Title Of<br>Agenda</h2></div>
  <div class="brand brand-sm"><i class="dot"></i>GiftHarbor</div>
  <ol class="agenda">
    <li><span>1.</span>Who We Are</li>
    <li><span>2.</span>What We Do</li>
    <li><span>3.</span>Our Process</li>
    <li><span>4.</span>Why Choose Us</li>
    <li><span>5.</span>Industries We Serve</li>
    <li><span>6.</span>Northwave Records</li>
    <li><span>7.</span>Parlor Magazine</li>
    <li><span>8.</span>Wishbright</li>
    <li><span>9.</span>Product Range</li>
    <li><span>10.</span>Let’s create together</li>
  </ol>
</section>

<!-- Who We Are -->
<section class="slide col-l row2">
  <div class="brand brand-sm"><i class="dot"></i>GiftHarbor</div>
  <h2 class="heading" style="top:60px">Who We Are</h2>
  <p class="body" style="top:86px;width:145px">GiftHarbor partners with brands and nonprofits to design, produce, and manage impactful merchandise programs that build engagement, raise awareness, and drive revenue.<br>We work with clients across corporate, nonprofit, and entertainment sectors transforming their vision into tangible, memorable products that resonate with their audiences.<br>We are two Retail &amp; Data Executives with a combined 25 years experience looking to streamline and perfect the merch experience.</p>
  <div class="ph" role="img" aria-label="Photo of a team joining fists over a table" style="left:242px;top:37px;width:83px;height:136px;border-radius:42px;background:linear-gradient(160deg,#8a6a52,#c99a7a 50%,#5b7a6a)"></div>
  <div class="ph" role="img" aria-label="Photo of colleagues giving a high five in an office" style="left:331px;top:79px;width:83px;height:135px;border-radius:42px;background:linear-gradient(160deg,#dfe6ea,#7a8d92 50%,#2e5660)"></div>
  <div class="footer"><div class="band"></div><span class="mail">✉ info@giftharbor.us</span><span class="page">Page 2</span></div>
</section>

<!-- What We Do -->
<section class="slide col-r row2">
  <div class="brand brand-sm"><i class="dot"></i>GiftHarbor</div>
  <svg class="abs" style="left:0;top:0" width="452" height="254" viewBox="0 0 452 254">
    <path d="M172 20 C178 60 190 80 206 100 C225 120 232 130 224 145 C210 170 180 180 170 225" fill="none" stroke="#3a7fc0" stroke-width=".7" stroke-dasharray="1.5 2"/>
  </svg>
  <div class="big-circle" style="left:37px;top:55px;width:128px;height:128px;font-size:13px">What We Do</div>
  <div class="service" style="left:191px;top:38px;width:178px"><div class="icon"><svg width="11" height="11" viewBox="0 0 12 12" fill="none" stroke="#111" stroke-width=".8"><path d="M2 10 L6 2 L10 10 Z"/><circle cx="6" cy="7" r="1.2"/></svg></div><h4>Design &amp; Sourcing</h4><p>Creative concepts and strategic product selection tailored to engage your target audience and strengthen brand recognition.</p></div>
  <div class="service" style="left:213px;top:75px;width:203px"><div class="icon"><svg width="11" height="11" viewBox="0 0 12 12" fill="none" stroke="#111" stroke-width=".8"><circle cx="6" cy="6" r="4"/><circle cx="6" cy="6" r="1.5"/></svg></div><h4>Custom Branded Merchandise</h4><p>High-quality, custom-designed products that authentically reflect your brand’s identity and message.</p></div>
  <div class="service" style="left:246px;top:112px;width:172px"><div class="icon"><svg width="11" height="11" viewBox="0 0 12 12" fill="none" stroke="#111" stroke-width=".8"><rect x="1.5" y="2" width="9" height="7"/><path d="M4 6 L6 4 L8 6"/></svg></div><h4>Ecommerce &amp; Fulfillment</h4><p>End-to-end management of online stores, inventory, and global shipping — ensuring a seamless customer experience from order to delivery.</p></div>
  <div class="service" style="left:213px;top:149px;width:205px"><div class="icon"><svg width="11" height="11" viewBox="0 0 12 12" fill="none" stroke="#111" stroke-width=".8"><circle cx="6" cy="6" r="2"/><path d="M1 1 L4 4 M11 1 L8 4 M1 11 L4 8 M11 11 L8 8"/></svg></div><h4>Cause-Based Campaigns</h4><p>Merchandise with purpose — fundraising products that generate revenue while amplifying your social impact or mission.</p></div>
  <div class="service" style="left:189px;top:186px;width:227px"><div class="icon"><svg width="11" height="11" viewBox="0 0 12 12" fill="none" stroke="#111" stroke-width=".8"><rect x="1.5" y="2" width="9" height="4"/><path d="M3 6 V10 M9 6 V10"/></svg></div><h4>Event Activations</h4><p>Large-scale branded experiences — from trade shows to corporate events, we deliver memorable merchandise that drives engagement.</p></div>
  <div class="footer"><div class="band"></div><span class="mail">✉ info@giftharbor.us</span><span class="page">Page 3</span></div>
</section>

<!-- Our Process -->
<section class="slide col-l row3">
  <div class="brand brand-sm"><i class="dot"></i>GiftHarbor</div>
  <h2 class="heading" style="top:72px">Our Process</h2>
  <div class="step" style="left:38px"><div class="icon"><svg width="10" height="10" viewBox="0 0 12 12" fill="none" stroke="#111" stroke-width="1"><circle cx="5" cy="5" r="3.5"/><path d="M7.5 7.5 L11 11"/></svg></div><h4>Discover</h4><p>Gain deep insight into your brand, goals, and audience through a collaborative discovery process. We listen, learn, and identify opportunities to align strategy with your vision.</p></div>
  <div class="step" style="left:137px"><div class="icon"><svg width="10" height="10" viewBox="0 0 12 12" fill="none" stroke="#111" stroke-width=".9"><circle cx="6" cy="5" r="3"/><path d="M4.5 10 H7.5"/></svg></div><h4>Design</h4><p>Gain deep insight into your brand, goals, and audience through a collaborative discovery process. We listen, learn, and identify opportunities to align strategy with your vision.</p></div>
  <div class="step" style="left:237px"><div class="icon"><svg width="10" height="10" viewBox="0 0 12 12" fill="none" stroke="#111" stroke-width=".9"><circle cx="6" cy="6" r="4.5"/><circle cx="6" cy="6" r="1.8"/></svg></div><h4>Produce</h4><p>Gain deep insight into your brand, goals, and audience through a collaborative discovery process. We listen, learn, and identify opportunities to align strategy with your vision.</p></div>
  <div class="step" style="left:336px"><div class="icon"><svg width="12" height="10" viewBox="0 0 14 12" fill="none" stroke="#111" stroke-width=".9"><rect x="1" y="2" width="8" height="6"/><path d="M9 4 H12 L13 6 V8 H9"/><circle cx="4" cy="9.5" r="1.2"/><circle cx="11" cy="9.5" r="1.2"/></svg></div><h4>Deliver</h4><p>Gain deep insight into your brand, goals, and audience through a collaborative discovery process. We listen, learn, and identify opportunities to align strategy with your vision.</p></div>
  <div class="footer"><div class="band"></div><span class="mail">✉ info@giftharbor.us</span><span class="page">Page 4</span></div>
</section>

<!-- Why Choose Us -->
<section class="slide col-r row3">
  <div class="brand brand-sm"><i class="dot"></i>GiftHarbor</div>
  <div class="big-circle" style="left:162px;top:55px;width:128px;height:128px;font-size:13px">Why Choose Us</div>
  <i class="node" style="left:185px;top:71px"></i><i class="node" style="left:266px;top:71px"></i>
  <i class="node" style="left:185px;top:167px"></i><i class="node" style="left:266px;top:167px"></i>
  <div class="reason left" style="left:63px;top:49px"><h4>Hands On Service</h4><p>No automated portals or impersonal vendors, just dedicated partnership and personalized attention to your unique needs</p></div>
  <div class="reason" style="left:306px;top:49px"><h4>Fast &amp; Transparent</h4><p>Quick turnaround times with clear, upfront pricing and no hidden fees or surprises</p></div>
  <div class="reason left" style="left:63px;top:146px"><h4>Premium Product Access</h4><p>Curated selection of sustainable, trending and high-quality product lines that elevate your brand</p></div>
  <div class="reason" style="left:306px;top:146px"><h4>Proven Track Record</h4><p>Trusted experience working with Fortune 500 companies and national non-profit organizations</p></div>
  <div class="footer"><div class="band"></div><span class="mail">✉ info@giftharbor.us</span><span class="page">Page 5</span></div>
</section>

<!-- Wishbright case -->
<section class="slide col-l row4">
  <div class="brand brand-sm"><i class="dot"></i>GiftHarbor</div>
  <h2 class="heading" style="top:61px">Wishbright</h2>
  <p class="body" style="top:86px;width:148px">GiftHarbor collaborated with Wishbright to create custom-branded apparel, volunteer gifts, and event giveaways that celebrated the organization’s mission while maximizing value through thoughtful sourcing and production. We provided fast turnarounds, reliable delivery, and white-glove service, ensuring every piece reflected the organization’s uplifting spirit. The result: meaningful merchandise that inspired donors and volunteers alike, helping Wishbright amplify its message of hope.</p>
  <div class="abs" style="left:272px;top:53px;width:148px;height:148px;border-radius:50%;background:#fff"></div>
  <div class="ph" role="img" aria-label="Photo of a volunteer in a blue event t-shirt, seen from behind" style="left:274px;top:71px;width:110px;height:110px;border-radius:50%;background:radial-gradient(circle at 50% 60%,#2d6fd0,#163f8f 60%,#3a2f2a)"></div>
  <div class="ph" role="img" aria-label="White baby onesie product photo" style="left:262px;top:54px;width:24px;height:28px;border-radius:6px;background:linear-gradient(160deg,#ffffff,#dfe4ea)"></div>
  <div class="ph" role="img" aria-label="Golf ball on tee product photo" style="left:386px;top:99px;width:26px;height:26px;border-radius:50%;background:radial-gradient(circle at 40% 35%,#ffffff,#cfd6dd)"></div>
  <div class="ph" role="img" aria-label="Black backpack product photo" style="left:244px;top:137px;width:30px;height:44px;border-radius:10px;background:linear-gradient(160deg,#2a2a2a,#0d0d0d)"></div>
  <div class="footer"><div class="band"></div><span class="mail">✉ info@giftharbor.us</span><span class="page">Page 6</span></div>
</section>

<!-- Closing -->
<section class="slide col-r row4">
  <div class="brand" style="font-size:17px;left:0;right:0;top:36px;justify-content:center"><i class="dot"></i>GiftHarbor</div>
  <div class="abs" style="left:170px;top:63px;width:112px;height:.6px;background:#9aa6c0"></div>
  <h2 class="cover-title" style="top:74px;font-size:15px">LET’S CREATE TOGETHER</h2>
  <p class="cover-title" style="top:102px;font-size:7px;line-height:10px;font-weight:500;color:var(--blue)">Ready to elevate your brand with custom merchandise?<br>Contact us to start your next program!</p>
  <div class="contact-disc">
    <span>Dean Harlow</span><span>dean@giftharbor.us</span><span>Nina Castell</span><span>nina@giftharbor.us</span>
  </div>
</section>

</body>
</html>
```